Business Card Design - Carrington Hill Lodge

We are looking at a new design for our business cards that has a modern and professional look. We run a residential aged care facility focussing on the care of residents. The cards will be used for potential clients, consultants and business opportunities in this sector. Blue and white is our main colours and would to see these colours incorporated in the design.
Industry/Entity Type
Business
Contact Information for Business Card
Carrington Hill Lodge, Darren Pelham, dpelham@carringtonhilllodge.com.au, Finance Manager, 0491 736 208, BCom, 48 Yarrabee Way, Kelvin Ridge, Qld 4215.

```html
<!DOCTYPE html>
<html lang="en">
<head>
<meta charset="utf-8">
<title>Carrington Hill Lodge – Business Card</title>
<link href="https://fonts.googleapis.com/css2?family=Open+Sans:wght@400;600&display=swap" rel="stylesheet">
<style>
  :root {
    --lodge-blue: #4a7b98;
    --lodge-taupe: #a89d96;
    --card-white: #ffffff;
    --ink: #4a4a4a;
    --page: #ecebe8;
  }
  * { box-sizing: border-box; margin: 0; padding: 0; }
  html, body { width: 1200px; height: 950px; overflow: hidden; }
  body {
    background: var(--page);
    font-family: "Open Sans", Arial, sans-serif;
    position: relative;
  }
  .card {
    position: absolute;
    top: 115px;
    width: 420px;
    height: 720px;
    border-radius: 26px;
    overflow: hidden;
    box-shadow: 0 6px 22px rgba(0,0,0,0.18);
  }
  .card-front { left: 150px; background: var(--card-white); }
  .card-back { left: 630px; background: var(--lodge-blue); }

  .front-header {
    height: 230px;
    background: var(--lodge-taupe);
    position: relative;
  }
  .brand-name {
    position: absolute;
    left: 0; right: 0; top: 120px;
    text-align: center;
    font-weight: 600;
    font-size: 26px;
    letter-spacing: 2px;
    text-transform: uppercase;
    color: var(--lodge-blue);
    background: var(--card-white);
    padding: 10px 0;
  }
  .brand-tagline {
    position: absolute;
    left: 20px; right: 20px; top: 188px;
    text-align: center;
    font-size: 17px;
    letter-spacing: 1px;
    color: var(--card-white);
  }

  .contact {
    text-align: center;
    padding-top: 34px;
    color: var(--ink);
  }
  .contact-icon { display: block; margin: 0 auto 6px; width: 20px; height: 20px; }
  .contact-icon path, .contact-icon circle { fill: var(--lodge-blue); }
  .person-name {
    font-weight: 600;
    font-size: 27px;
    color: var(--lodge-blue);
    line-height: 1.15;
  }
  .person-role { font-size: 19px; margin-bottom: 20px; }
  .contact-line { font-size: 18px; line-height: 1.35; margin-bottom: 20px; }

  .back-brand {
    position: absolute;
    left: 60px; right: 0; top: 330px;
    text-align: center;
    font-weight: 600;
    font-size: 26px;
    letter-spacing: 2px;
    text-transform: uppercase;
    color: var(--card-white);
    line-height: 1.3;
  }
  .back-web {
    position: absolute;
    left: 40px; top: 360px;
    transform-origin: left top;
    transform: rotate(90deg) translate(-50%, -100%);
    white-space: nowrap;
    font-size: 19px;
    color: var(--card-white);
  }
</style>
</head>
<body>
  <section class="card card-front">
    <header class="front-header">
      <div class="brand-name">Carrington Hill Lodge</div>
      <div class="brand-tagline">Comfort, Respect, Community</div>
    </header>
    <div class="contact">
      <svg class="contact-icon" viewBox="0 0 20 20"><circle cx="10" cy="6" r="4.5"/><path d="M2 19c0-5 3.5-7.5 8-7.5s8 2.5 8 7.5z"/></svg>
      <div class="person-name">Darren Pelham BCom</div>
      <div class="person-role">Finance Manager</div>

      <svg class="contact-icon" viewBox="0 0 20 20"><path d="M10 1a6 6 0 0 0-6 6c0 4.5 6 12 6 12s6-7.5 6-12a6 6 0 0 0-6-6zm0 8.5a2.5 2.5 0 1 1 0-5 2.5 2.5 0 0 1 0 5z"/></svg>
      <div class="contact-line">48 Yarrabee Way<br>Kelvin Ridge, Qld 4215.</div>

      <svg class="contact-icon" viewBox="0 0 20 20"><path d="M5 1.5l3 4-2 2.2c1 2.3 2.8 4.2 5.3 5.3l2.2-2 4 3-1.5 3.5C9 17.5 2.5 11 1.5 3z"/></svg>
      <div class="contact-line">0491 736 208</div>

      <svg class="contact-icon" viewBox="0 0 20 20"><path d="M1 4h18v1.5l-9 6-9-6z"/><path d="M1 7.5l9 6 9-6V16H1z"/></svg>
      <div class="contact-line">dpelham@carringtonhilllodge.com.au</div>

      <svg class="contact-icon" viewBox="0 0 20 20"><path d="M10 1a9 9 0 1 0 0 18 9 9 0 0 0 0-18zm0 2c1 1.3 1.8 3.3 2 6H8c.2-2.7 1-4.7 2-6zM3.1 9a7 7 0 0 1 3.4-5.1C6 5.3 5.5 7 5.4 9zm0 2h2.3c.1 2 .6 3.7 1.1 5.1A7 7 0 0 1 3.1 11zM10 17c-1-1.3-1.8-3.3-2-6h4c-.2 2.7-1 4.7-2 6zm3.5-.9c.6-1.4 1-3.1 1.1-5.1h2.3a7 7 0 0 1-3.4 5.1zm1.1-7.1c-.1-2-.6-3.7-1.1-5.1A7 7 0 0 1 16.9 9z"/></svg>
      <div class="contact-line">www.carringtonhilllodge.com.au</div>
    </div>
  </section>

  <section class="card card-back">
    <div class="back-web">www.carringtonhilllodge.com.au</div>
    <div class="back-brand">Carrington<br>Hill Lodge</div>
  </section>
</body>
</html>
```